Destination Wedding Photographer

I am a Wedding photographer based in San Juan, Puerto Rico. The banner will be shown in the United States to brides that plan to have their wedding in Puerto Rico.

I want to highlight the following words/phrases
Puerto Rico
Destination Wedding
Photographer
(in that order)

feel free to get creative adding your own inspired text.

My web site: www.benitolavarro.com

Target Market(s)

Brides in the united states looking for a photographer for their wedding in Puerto Rico

Industry/Entity Type

Wedding

Requirements
Must have
• + Your ad must be a .gif, .png or .jpg smaller than 40kb in filesize
+ include the following sizes: 300x250, 728x90, 160x600, 468x60, or 120x600
+ Your ad must include the advertiser's brand
+ Your ad must have a border
Should not have
• + Your ad cannot imitate computer effects like scrolling or mousing over
+ No animations longer than 30 seconds
+ No strobe or flashing effects allowed
+ Your ad and campaign must not feature or promote alcohol, anabolic steroids, drugs, financial products, gambling, adult content, or weight loss products

```html
<!DOCTYPE html>
<html lang="en">
<head>
<meta charset="UTF-8">
<title>Benito Lavarro Photography – Destination Wedding Photographer, Puerto Rico</title>
<link rel="stylesheet" href="https://fonts.googleapis.com/css2?family=Comfortaa:wght@400&family=Open+Sans:ital,wght@1,700&display=swap">
<style>
  :root {
    --sky-top: #2a73bd;
    --sky-mid: #4c95d6;
    --sky-horizon: #8cc2ea;
    --haze: rgba(255, 255, 255, 0.35);
    --grass-light: #8fb33a;
    --grass-dark: #4f7a1c;
    --border: #8a8f96;
    --text: #ffffff;
    --text-shadow: rgba(10, 40, 80, 0.35);
  }

  * { margin: 0; padding: 0; box-sizing: border-box; }

  html, body {
    width: 1200px;
    height: 320px;
    overflow: hidden;
    background: #ffffff;
  }

  .banner {
    position: relative;
    width: 1200px;
    height: 320px;
    border: 2px solid var(--border);
    overflow: hidden;
  }

  .banner__photo {
    position: absolute;
    inset: 0;
    background:
      radial-gradient(ellipse 380px 200px at 330px 210px, var(--haze), transparent 70%),
      linear-gradient(to top left, var(--sky-top) 0%, var(--sky-mid) 45%, var(--sky-horizon) 100%);
  }

  .banner__grass {
    position: absolute;
    left: 0;
    bottom: 0;
    width: 100%;
    height: 60px;
  }

  .brand {
    position: absolute;
    left: 760px;
    top: 62px;
    width: 410px;
    text-align: center;
    color: var(--text);
    font-family: "Comfortaa", sans-serif;
    font-weight: 400;
    text-shadow: 0 1px 3px var(--text-shadow);
  }

  .brand__name {
    display: block;
    font-size: 58px;
    line-height: 1.1;
    letter-spacing: -1px;
  }

  .brand__trade {
    display: block;
    margin-top: 14px;
    font-size: 20px;
    letter-spacing: 8px;
    text-transform: uppercase;
  }

  .location {
    position: absolute;
    left: 314px;
    top: 216px;
    color: var(--text);
    font-family: "Comfortaa", sans-serif;
    font-weight: 400;
    font-size: 46px;
    letter-spacing: -0.5px;
    text-shadow: 0 1px 3px var(--text-shadow);
  }

  .tagline {
    position: absolute;
    left: 764px;
    top: 238px;
    color: var(--text);
    font-family: "Open Sans", sans-serif;
    font-style: italic;
    font-weight: 700;
    font-size: 23px;
    text-shadow: 0 1px 3px var(--text-shadow);
  }
</style>
</head>
<body>
  <div class="banner">
    <div class="banner__photo" role="img" aria-label="Photograph of a bride and groom dancing in a dip pose on a grassy hilltop under a clear blue sky">
      <svg class="banner__grass" viewBox="0 0 1200 60" preserveAspectRatio="none" aria-hidden="true">
        <defs>
          <linearGradient id="grass-fill" x1="0" y1="0" x2="0" y2="1">
            <stop offset="0" stop-color="var(--grass-light)"/>
            <stop offset="1" stop-color="var(--grass-dark)"/>
          </linearGradient>
        </defs>
        <path d="M0 22 Q300 10 600 20 T1200 26 L1200 60 L0 60 Z" fill="url(#grass-fill)"/>
      </svg>
    </div>

    <div class="brand">
      <span class="brand__name">Benito Lavarro</span>
      <span class="brand__trade">Photography</span>
    </div>

    <p class="location">Puerto Rico</p>
    <p class="tagline">Destination Wedding Photographer</p>
  </div>
</body>
</html>
```